New business stationairy

I need paper with header and footer and business cards.
I am a Ltd Company and my main field of expertise is QA/QC inspection in the Oil and Gas Industry. I will need all contact detail inserted and a footer with registration number and bank details etc

Business

```html
<!DOCTYPE html>
<html lang="en">
<head>
<meta charset="utf-8">
<title>Harlow Inspection Services Ltd – Stationery</title>
<link href="https://fonts.googleapis.com/css2?family=Orbitron:wght@500;600&family=Tinos:wght@400;700&family=Open+Sans:wght@600;700&display=swap" rel="stylesheet">
<style>
  :root {
    --brand-blue: #3d3fd6;
    --brand-navy: #1f2260;
    --rule-blue: #6f73e8;
    --ink: #111111;
    --paper: #ffffff;
    --backdrop: #2b1d14;
  }
  * { box-sizing: border-box; margin: 0; padding: 0; }
  html, body { width: 1043px; height: 1200px; overflow: hidden; }
  body { background: var(--backdrop); position: relative; font-family: "Open Sans", sans-serif; }

  .letterhead {
    position: absolute; left: 131px; top: 50px;
    width: 780px; height: 1100px;
    background: var(--paper);
    box-shadow: 0 10px 30px rgba(0,0,0,.45);
  }
  .letterhead__brand {
    position: absolute; left: 46px; top: 52px;
    display: flex; align-items: center; gap: 12px;
    white-space: nowrap;
  }
  .brand-dot { width: 22px; height: 22px; border-radius: 50%; background: var(--brand-navy); flex: none; }
  .letterhead__name {
    font-family: "Orbitron", sans-serif; font-weight: 600;
    font-size: 24px; letter-spacing: 1px; color: var(--brand-blue);
    white-space: nowrap;
  }
  .letterhead__rule-top {
    position: absolute; left: 30px; right: 30px; top: 96px;
    height: 2px; background: var(--rule-blue);
  }
  .letterhead__contact {
    position: absolute; left: 46px; top: 106px;
    font-size: 11px; font-weight: 700; line-height: 1.3; color: var(--ink);
  }
  .letterhead__address {
    position: absolute; right: 40px; text-align: right;
    font-size: 11px; font-weight: 700; line-height: 1.3; color: var(--ink);
  }
  .letterhead__address--upper { top: 40px; }
  .letterhead__address--lower { top: 106px; }
  .letterhead__rule-right {
    position: absolute; left: 745px; top: 160px; width: 2px; height: 330px;
    background: var(--rule-blue);
  }
  .letterhead__rule-left {
    position: absolute; left: 50px; top: 620px; width: 2px; height: 420px;
    background: var(--rule-blue);
  }
  .letterhead__rule-bottom {
    position: absolute; left: 30px; right: 30px; top: 1050px;
    height: 2px; background: var(--rule-blue);
  }
  .letterhead__footer {
    position: absolute; left: 50px; right: 50px; top: 1062px;
    display: flex; justify-content: space-between;
    font-family: "Orbitron", sans-serif; font-weight: 500;
    font-size: 12px; letter-spacing: 1px; color: var(--ink);
  }

  .business-card {
    position: absolute; left: 125px; top: 440px;
    width: 530px; height: 300px;
    background: var(--paper);
    box-shadow: 0 4px 16px rgba(0,0,0,.35);
    font-family: "Tinos", serif; color: var(--ink);
  }
  .business-card__brand {
    position: absolute; left: 22px; top: 24px;
    display: flex; align-items: center; gap: 10px;
    white-space: nowrap;
  }
  .business-card__brand .brand-dot { width: 18px; height: 18px; }
  .business-card__name {
    font-family: "Orbitron", sans-serif; font-weight: 600;
    font-size: 17px; letter-spacing: 1px; color: var(--brand-navy);
  }
  .business-card__rule-top {
    position: absolute; left: 22px; top: 62px; width: 470px; height: 1px;
    background: var(--rule-blue);
  }
  .business-card__rule-right {
    position: absolute; left: 502px; top: 10px; width: 3px; height: 122px;
    background: var(--brand-navy);
  }
  .business-card__person {
    position: absolute; left: 40px; top: 116px; text-align: center; width: 150px;
  }
  .business-card__person-name { font-size: 18px; font-weight: 700; color: var(--brand-blue); }
  .business-card__person-role { font-size: 17px; font-weight: 700; margin-top: 2px; }
  .business-card__address {
    position: absolute; right: 42px; top: 88px; text-align: right;
    font-size: 17px; line-height: 1.17; font-style: normal;
  }
  .business-card__rule-mid {
    position: absolute; left: 22px; top: 222px; width: 480px; height: 1px;
    background: var(--brand-navy);
  }
  .business-card__rule-left {
    position: absolute; left: 20px; top: 214px; width: 3px; height: 78px;
    background: var(--brand-navy);
  }
  .business-card__contact {
    position: absolute; left: 0; right: 0; top: 240px; text-align: center;
    font-size: 17px; line-height: 1.2;
  }
</style>
</head>
<body>
  <main class="letterhead">
    <div class="letterhead__brand">
      <span class="brand-dot"></span>
      <span class="letterhead__name">HARLOW INSPECTION SERVICES LTD</span>
    </div>
    <div class="letterhead__address letterhead__address--upper">The Willows<br>Mill Lane<br>Ashby</div>
    <div class="letterhead__rule-top"></div>
    <div class="letterhead__contact">Email: maren.holt@example.co.uk<br>mobile: 07700900123</div>
    <div class="letterhead__address letterhead__address--lower">Fernbrook<br>Wessex<br>WX4 7QL</div>
    <div class="letterhead__rule-right"></div>
    <div class="letterhead__rule-left"></div>
    <div class="letterhead__rule-bottom"></div>
    <footer class="letterhead__footer">
      <span>Company Registration Number : 4718260</span>
      <span>|</span>
      <span>Bank Details: 40516273</span>
    </footer>

    <section class="business-card">
      <div class="business-card__brand">
        <span class="brand-dot"></span>
        <span class="business-card__name">HARLOW INSPECTION SERVICES LTD</span>
      </div>
      <div class="business-card__rule-top"></div>
      <div class="business-card__rule-right"></div>
      <div class="business-card__person">
        <div class="business-card__person-name">Maren Holt</div>
        <div class="business-card__person-role">Director</div>
      </div>
      <address class="business-card__address">
        The Willows<br>Mill Lane<br>Ashby<br>Fernbrook<br>Wessex<br>WX4 7QL
      </address>
      <div class="business-card__rule-mid"></div>
      <div class="business-card__rule-left"></div>
      <div class="business-card__contact">Email: maren.holt@example.co.uk<br>mobile: 07700900123</div>
    </section>
  </main>
</body>
</html>
```